Brookvale Health Solutions

I need a professional and informational website for healthcare professionals. Please make the website the same style and content as our attached pdf.

Target Market(s)

Medical doctors

Industry/Entity Type

Healthcare

Coding

Coded - Design and coding required

Number of Pages Required

4 page

Requirements
Must have
• The same style and content as the uploaded powerpoints

```html
<!DOCTYPE html>
<html lang="en">
<head>
<meta charset="utf-8">
<title>About Us — Brookvale Health Solutions</title>
<link href="https://fonts.googleapis.com/css2?family=Inter:wght@400;500;600;700&family=Plus+Jakarta+Sans:wght@600;700;800&display=swap" rel="stylesheet">
<style>
:root{
  --ink:#020b1f;
  --navy:#041735;
  --teal:#146b6b;
  --teal-soft:#a6ecef;
  --text:#3a3f4a;
  --muted:#6b7280;
  --hero-bg:#f7f8fa;
  --band-bg:#f2f3f5;
  --card-bg:#eceef0;
  --line:#d9dde2;
  --footer-link:#7d879a;
}
*{box-sizing:border-box;margin:0;padding:0}
html,body{width:1200px;height:2976px;overflow:hidden}
body{position:relative;font-family:"Inter",sans-serif;color:var(--text);background:#fff}
.abs{position:absolute}
.display{font-family:"Plus Jakarta Sans",sans-serif}

/* header */
.site-header{left:0;top:0;width:1200px;height:73px;background:#fff;border-bottom:1px solid #eef0f2}
.brand{left:42px;top:14px;color:var(--ink);font-family:"Plus Jakarta Sans",sans-serif;font-weight:800;line-height:1}
.brand-name{display:block;font-size:28px;letter-spacing:-0.5px}
.brand-sub{display:block;font-size:10px;margin-top:2px;padding-left:26px}
.nav a{position:absolute;top:28px;font-size:16px;color:#444b57;text-decoration:none}
.nav .active{color:var(--teal);font-weight:500;border-bottom:2px solid var(--teal);padding-bottom:2px}
.btn-contact{left:1067px;top:20px;width:91px;height:34px;background:var(--ink);color:#fff;font-weight:600;font-size:15px;display:flex;align-items:center;justify-content:center;border-radius:2px}

/* hero */
.hero{left:0;top:73px;width:1200px;height:673px;background:var(--hero-bg)}
.eyebrow{left:42px;top:216px;background:var(--teal-soft);color:var(--teal);font-size:11px;font-weight:700;letter-spacing:1.4px;padding:4px 11px}
.hero-title{left:42px;top:262px;font-size:70px;font-weight:800;line-height:66px;letter-spacing:-3px;color:var(--ink)}
.hero-title em{font-style:normal;color:var(--teal)}
.hero-copy{left:42px;top:486px;width:620px;font-size:19px;line-height:29.5px;color:#3b404b}
.hero-photo{left:719px;top:190px;width:439px;height:439px;border-radius:6px;background:linear-gradient(180deg,#cfcfcf 0%,#e3e3e3 55%,#bdbdbd 70%,#dcdcdc 100%);box-shadow:0 20px 40px rgba(0,0,0,.12)}
.stat-card{left:697px;top:539px;width:302px;height:112px;background:var(--navy);border-radius:4px;color:#fff;padding:28px 29px}
.stat-num{font-family:"Plus Jakarta Sans",sans-serif;font-weight:800;font-size:34px;line-height:1}
.stat-label{font-size:13px;letter-spacing:1.8px;margin-top:6px}

/* leadership */
.leadership{left:0;top:746px;width:1200px;height:855px;background:var(--band-bg)}
.section-title{font-size:30px;font-weight:700;color:var(--ink);letter-spacing:-0.3px}
.section-sub{font-size:16px;color:#444b57}
.rule{left:350px;top:899px;width:777px;height:1px;background:#e2e5e9}
.member{width:349px}
.member-photo{width:349px;height:435px;position:relative}
.member-tag{position:absolute;left:20px;bottom:14px;background:var(--ink);color:#fff;font-size:10px;font-weight:700;letter-spacing:1.2px;padding:4px 9px}
.member-name{font-family:"Plus Jakarta Sans",sans-serif;font-weight:700;font-size:20px;color:var(--ink);margin-top:24px}
.member-role{font-size:13px;color:var(--teal);font-weight:500;margin-top:3px}
.member-bio{font-size:13.5px;line-height:21px;color:#4a4f5a;margin-top:16px}

/* inquiries */
.field-label{font-size:10px;font-weight:700;letter-spacing:1.2px;color:var(--ink)}
.field{border:1px solid var(--line);background:#fff;font-size:15px;color:#7b818c;padding:0 12px;display:flex;align-items:center}
.field.area{align-items:flex-start;padding-top:12px}
.btn-send{left:42px;top:2121px;width:193px;height:51px;background:var(--ink);color:#fff;font-weight:700;font-size:15px;display:flex;align-items:center;justify-content:center;gap:8px;border-radius:2px;box-shadow:0 4px 10px rgba(2,11,31,.2)}
.info-card{width:246px;height:184px;background:var(--card-bg);border-radius:4px;padding:28px 29px}
.info-title{font-family:"Plus Jakarta Sans",sans-serif;font-weight:700;font-size:16px;color:var(--ink);margin-top:14px}
.info-text{font-size:13.5px;line-height:21px;color:#4a4f5a;margin-top:6px}
.map-card{left:637px;top:1917px;width:521px;height:522px;background:linear-gradient(180deg,#dcdde0,#d3d5d8);border-radius:4px}
.map-chip{left:968px;top:2396px;width:176px;height:28px;background:#fff;border-radius:3px;font-size:10px;font-weight:700;letter-spacing:1.2px;color:var(--ink);display:flex;align-items:center;justify-content:center}

/* footer */
.site-footer{left:0;top:2526px;width:1200px;height:450px;background:var(--ink)}
.footer-brand{left:42px;top:2598px;color:#fff;font-family:"Plus Jakarta Sans",sans-serif;font-weight:800;line-height:1}
.footer-brand .brand-name{font-size:24px}
.footer-brand .brand-sub{font-size:9px;padding-left:22px}
.footer-about{left:42px;top:2663px;width:380px;font-size:15px;line-height:23.5px;color:#7d879a}
.footer-col h4{font-size:15px;font-weight:500;color:var(--teal);margin-bottom:18px}
.footer-col a{display:block;font-size:13px;color:var(--footer-link);text-decoration:none;margin-bottom:14.5px}
.social{width:37px;height:36px;background:#0d2448;display:flex;align-items:center;justify-content:center;color:#fff;font-size:12px}
.footer-rule{left:42px;top:2861px;width:1116px;height:1px;background:#131d33}
.legal{top:2893px;font-size:10px;letter-spacing:1.2px;color:#59647a}
</style>
</head>
<body>

<header class="site-header abs">
  <div class="brand abs"><span class="brand-name">BROOKVALE</span><span class="brand-sub">Health Solutions</span></div>
  <nav class="nav">
    <a style="left:756px">Home</a>
    <a class="active" style="left:827px;top:27px">About Us</a>
    <a style="left:920px">Clinical Solutions</a>
  </nav>
  <div class="btn-contact abs">Contact</div>
</header>

<section class="hero abs"></section>
<div class="eyebrow abs">OUR MISSION</div>
<h1 class="hero-title display abs">Advancing Clinical<br><em>Precision</em> with<br>Integrity.</h1>
<p class="hero-copy abs">Founded in 2014, Brookvale Health Solutions was established to bridge the gap between complex medical data and actionable clinical insights. We believe that every diagnostic decision should be supported by the highest standard of data integrity and architectural excellence.</p>
<div class="hero-photo abs" role="img" aria-label="Bright white clinical room with a cabinet and medical equipment"></div>
<div class="stat-card abs"><div class="stat-num">10+</div><div class="stat-label">YEARS OF CLINICAL EXCELLENCE</div></div>

<section class="leadership abs"></section>
<h2 class="section-title display abs" style="left:42px;top:830px">Medical Leadership</h2>
<p class="section-sub abs" style="left:42px;top:880px">Guided by practitioners, for practitioners.</p>
<div class="rule abs"></div>

<article class="member abs" style="left:42px;top:958px">
  <div class="member-photo" role="img" aria-label="Portrait of the chief medical officer in a dark suit" style="background:linear-gradient(160deg,#2f4a55,#132129 70%,#1c2c36)">
    <span class="member-tag">CHIEF MEDICAL OFFICER</span>
  </div>
  <h3 class="member-name">Dr. Halvorsen</h3>
  <p class="member-role">CMO &amp; Strategy Lead</p>
  <p class="member-bio">An innovator in clinical informatics with over 20 years of experience in tertiary care systems.</p>
</article>

<article class="member abs" style="left:427px;top:958px">
  <div class="member-photo" role="img" aria-label="Portrait of the head of clinical research in a blue shirt" style="background:linear-gradient(160deg,#14413f,#1f5a58 50%,#7b9ab8)"></div>
  <h3 class="member-name">Dr. Miriam Okafor</h3>
  <p class="member-role">Head of Clinical Research</p>
  <p class="member-bio">Specializing in data-driven diagnostic protocols and cross-institutional research frameworks.</p>
</article>

<article class="member abs" style="left:810px;top:958px">
  <div class="member-photo" role="img" aria-label="Portrait of the director of operations in a navy suit" style="background:linear-gradient(160deg,#9fb4b4,#8aa3a6 55%,#1e2f47)"></div>
  <h3 class="member-name">Owen Lachlan</h3>
  <p class="member-role">Director of Operations</p>
  <p class="member-bio">Streamlining healthcare delivery through lean methodologies and robust technological integration.</p>
</article>

<h2 class="section-title display abs" style="left:42px;top:1686px">Professional Inquiries</h2>
<p class="section-sub abs" style="left:42px;top:1729px">Submit a formal request for clinical collaboration or support.</p>

<label class="field-label abs" style="left:42px;top:1795px">FULL NAME</label>
<div class="field abs" style="left:42px;top:1815px;width:247px;height:36px">e.g. Dr. Renata Cole</div>
<label class="field-label abs" style="left:318px;top:1795px">MEDICAL LICENSE / ID</label>
<div class="field abs" style="left:318px;top:1815px;width:246px;height:36px">Optional</div>
<label class="field-label abs" style="left:42px;top:1883px">INSTITUTIONAL EMAIL</label>
<div class="field abs" style="left:42px;top:1903px;width:522px;height:36px">doctor@brookvalehealth.com</div>
<label class="field-label abs" style="left:42px;top:1971px">NATURE OF INQUIRY</label>
<div class="field area abs" style="left:42px;top:1989px;width:522px;height:102px">How may our clinical team assist you?</div>
<div class="btn-send abs">Send Message <span>&#8594;</span></div>

<div class="info-card abs" style="left:637px;top:1689px">
  <svg width="18" height="20" viewBox="0 0 18 20" fill="none" stroke="#146b6b" stroke-width="1.8"><path d="M9 19s-7-6.2-7-11a7 7 0 0 1 14 0c0 4.8-7 11-7 11z"/><circle cx="9" cy="8" r="2.4"/></svg>
  <h3 class="info-title">Clinical HQ</h3>
  <p class="info-text">1420 Harbourline Avenue<br>Suite 210, East Wing<br>Millbrook, CA 94550</p>
</div>
<div class="info-card abs" style="left:912px;top:1689px">
  <svg width="19" height="19" viewBox="0 0 24 24" fill="none" stroke="#146b6b" stroke-width="2" stroke-linejoin="round"><path d="M5 3h4l2 5-2.5 1.5a11 11 0 0 0 6 6L16 13l5 2v4a2 2 0 0 1-2 2A16 16 0 0 1 3 5a2 2 0 0 1 2-2z"/></svg>
  <h3 class="info-title">Clinical Support</h3>
  <p class="info-text">Main: (555) 014-2270<br>Urgent: (555) 014-7731<br>Secure Fax: (555) 014-2271</p>
</div>

<div class="map-card abs" role="img" aria-label="Framed city street map with the headquarters location marked"></div>
<div class="map-chip abs">SATELLITE PRECISION VIEW</div>

<footer class="site-footer abs"></footer>
<div class="footer-brand abs"><span class="brand-name">BROOKVALE</span><span class="brand-sub">Health Solutions</span></div>
<p class="footer-about abs">The clinical atelier for modern healthcare systems. We provide the architectural backbone for the next generation of medical practitioners.</p>
<div class="footer-col abs" style="left:622px;top:2600px">
  <h4>Solutions</h4>
  <a>Diagnostic Frameworks</a><a>Patient Record Integrity</a><a>Clinical Informatics</a><a>Bespoke Research</a>
</div>
<div class="footer-col abs" style="left:912px;top:2600px">
  <h4>Platform</h4>
  <a>About &amp; History</a><a>Leadership</a><a>Contact Support</a><a>Legal &amp; Privacy</a>
</div>
<div class="social abs" style="left:42px;top:2802px">
  <svg width="12" height="12" viewBox="0 0 12 12" fill="none" stroke="#fff" stroke-width="1.3"><circle cx="9.5" cy="2.5" r="1.5"/><circle cx="2.5" cy="6" r="1.5"/><circle cx="9.5" cy="9.5" r="1.5"/><path d="M4 5.2l4-2M4 6.8l4 2"/></svg>
</div>
<div class="social abs" style="left:92px;top:2802px">@</div>
<div class="footer-rule abs"></div>
<p class="legal abs" style="left:42px">© 2024 BROOKVALE HEALTH SOLUTIONS. ALL RIGHTS RESERVED.</p>
<p class="legal abs" style="left:942px">PRIVACY POLICY</p>
<p class="legal abs" style="left:1058px">TERMS OF SERVICE</p>

</body>
</html>
```